Business card - house cleaning company

We want friendly high end business card highlighting our services . NO LOGOs on back of card please.. no vertical cards NO DOUBLE BROOMS

2 owners of the company: Corinne Halvey & Joel Brandt

Included phone number: (555)318-2047

Email: brightlanetidy@mailnest.example

Website: www.brightlanetidy.example

Bonded & Insured

Alder Ridge, CO 80999

Slogan maybe: Bringing a brighter shine to every corner of home

We want elegant high end card for house cleaning service. Maybe 2 sided if needed. Can it have bullet points of some services we offer

Residential Home Cleaning
Vacation Rental Cleaning
Commercial Cleaning
Carpet Cleaning
Window Cleaning
Property Management
Property Inspections
Property Maintenance
Trash Removal
Concierge Services

Highlight service on back of card. If we can do a one sided card with all this that’s great as well. Not cartoony.

Our logo attached and a design somone I had Perrin but they put very little time in. Not Unique enough. If you can do a custom design with a feminine touch that be great.

You will be eliminated for not reading the brief. NO DOUBLE LOGOS NO DOUBLE BROOMS. PLEASE BE CREATIVE. IF POST SAME LOGO WITH SMAL CHANGES RHEY WILL BE ELIMINATED. BE CREATIVE.

Thank you everyone for your designs. please only use the logo 1 time. and would love to see some that dont look all the same. We appreciate your time.

Target Market(s)

Residential and vacation rental home cleaning maid service

Industry/Entity Type

House cleaning maid services

Contact Information for Business Card

For business card use logo. black and green one provided. others for example. I wil try find some example.. We want friendly high end look. 2 owners of the company: Corinne Halvey & Joel Brandt Included phone number: (555)318-2047 Email: brightlanetidy@mailnest.example Website: www.brightlanetidy.example Bonded & Insured Estes Park, CO Slogan maybe: Bringing a brighter shine to every corner of home or Quality Service Guaranteed We want elegant high end card for house cleaning service. Maybe 2 sided if needed. Can it have bullet points of some services we offer Residential Home Cleaning Vacation Rental Cleaning Commercial Cleaning Carpet Cleaning Window Cleaning Property Management Property Inspections Property Maintenance Trash Removal Concierge Services

Requirements
Must have
• For business card use logo . Creativity. black and green one provided. We want friendly high end look. 2 owners of the company: Corinne Halvey & Joel Brandt Included phone number: (555)318-2047 Email: brightlanetidy@mailnest.example Website: www.brightlanetidy.example Licensed Bonded & Insured Estes Park, CO Slogan maybe: Bringing a brighter shine to every corner of home or Quality Service Guaranteed We want elegant high end card for house cleaning service. Maybe 2 sided if needed. Can it have bullet points of some services we offer Residential Home Cleaning Vacation Rental Cleaning Commercial Cleaning Carpet Cleaning Window Cleaning Property Management Property Inspections Property Maintenance Trash Removal Concierge Services .. creatitivty a plus. whimsical. we like stars..
Nice to have
• we want much better than the example of biz card provided as example. logo has colors that are in our website palette as well. We are open to ideas for the business card design. Will pay tip to best work. PLEASE USE COMPLIMENTING COLORS. . WE LIKE BLACK AND WHITE, stars
Should not have
• NO DOUBLE LOGOS. READ READ. READ. YOU WILL BE ELIMINATED no double logos or double brooms same side of card. I want didfrent examples. please don't make all your submission look the same

```html
<!DOCTYPE html>
<html lang="en">
<head>
<meta charset="utf-8">
<title>Bright Lane Cleaning Services – Business Card</title>
<link href="https://fonts.googleapis.com/css2?family=Lato:wght@400;700&display=swap" rel="stylesheet">
<style>
  :root {
    --backdrop: #b3b3b3;
    --leaf: #6f9544;
    --ink: #000000;
    --paper: #ffffff;
  }
  * { margin: 0; padding: 0; box-sizing: border-box; }
  html, body {
    width: 1200px; height: 1200px; overflow: hidden;
    background: var(--backdrop);
    font-family: "Lato", sans-serif;
    color: var(--ink);
  }
  .stage { position: relative; width: 1200px; height: 1200px; }

  /* Back of card: services */
  .card-back {
    position: absolute; left: 255px; top: 175px;
    width: 690px; height: 393px;
    background: var(--leaf);
  }
  .services {
    position: absolute; top: 164px;
    list-style: none;
    font-size: 17px; line-height: 24px;
    text-transform: uppercase;
  }
  .services li { position: relative; white-space: nowrap; }
  .services li::before {
    content: ""; position: absolute; top: 7px;
    width: 10px; height: 10px; border-radius: 50%;
    background: var(--ink);
  }
  .services--left { left: 53px; }
  .services--left li::before { left: -20px; }
  .services--right { right: 56px; text-align: right; }
  .services--right li::before { right: -22px; }
  .slogan {
    position: absolute; left: 0; right: 0; top: 332px;
    text-align: center;
    font-size: 19px; font-weight: 700;
    text-transform: uppercase; letter-spacing: -0.2px;
  }

  /* Front of card: brand and contact */
  .card-front {
    position: absolute; left: 255px; top: 632px;
    width: 690px; height: 393px;
    background: var(--paper);
    overflow: hidden;
  }
  .card-front__panel {
    position: absolute; left: 345px; top: 0;
    width: 345px; height: 393px;
    background: var(--ink);
  }
  .card-front__ribbon {
    position: absolute; left: 330px; top: 56px;
    width: 30px; height: 270px;
  }
  .brand-name {
    position: absolute; left: 0; width: 330px; top: 175px;
    text-align: center;
    font-size: 25px; font-weight: 700; line-height: 30px;
    color: var(--ink);
    text-transform: uppercase; letter-spacing: 1px;
  }
  .owner {
    position: absolute; right: 45px; top: 96px;
    text-align: right;
  }
  .owner__name {
    font-size: 31px; font-weight: 700; line-height: 34px;
    color: var(--leaf);
  }
  .owner__role {
    font-size: 17px; color: var(--paper); line-height: 20px;
    text-transform: uppercase;
  }
  .contact {
    position: absolute; right: 26px; top: 218px;
    list-style: none; text-align: right;
    font-size: 16.5px; color: var(--paper);
  }
  .contact li {
    display: flex; justify-content: flex-end; align-items: center;
    height: 28.5px; gap: 1px; white-space: nowrap;
  }
  .contact .icon { width: 18px; height: 18px; flex: none; }
  .contact .no-icon { padding-right: 19px; }
</style>
</head>
<body>
<main class="stage">

  <section class="card-back" aria-label="Card back with services">
    <ul class="services services--left">
      <li>Residential Home Cleaning</li>
      <li>Vacation Rental Cleaning</li>
      <li>Commercial Cleaning</li>
      <li>Carpet Cleaning</li>
      <li>Window Cleaning</li>
    </ul>
    <ul class="services services--right">
      <li>Property Management</li>
      <li>Property Inspections</li>
      <li>Property Maintence</li>
      <li>Trash Removal</li>
      <li>Concierge Services</li>
    </ul>
    <p class="slogan">Bringing a brighter shine to every corner of home</p>
  </section>

  <section class="card-front" aria-label="Card front with contact details">
    <div class="card-front__panel"></div>
    <svg class="card-front__ribbon" viewBox="0 0 30 270" aria-hidden="true">
      <polygon points="0,10 15,1 15,10" fill="#6f9544"/>
      <rect x="0" y="10" width="30" height="260" fill="#6f9544"/>
    </svg>

    <p class="brand-name">Bright Lane<br>Cleaning Services</p>

    <div class="owner">
      <p class="owner__name">Corinne Halvey</p>
      <p class="owner__role">Owner</p>
    </div>

    <ul class="contact">
      <li>(555) 318-2047
        <svg class="icon" viewBox="0 0 20 20" aria-hidden="true"><circle cx="10" cy="10" r="10" fill="#6f9544"/><path d="M6.5 5.2c.5-.4 1.1-.3 1.4.2l.9 1.6c.2.4.1.9-.2 1.2l-.6.5c.5 1.1 1.4 2 2.5 2.5l.5-.6c.3-.3.8-.4 1.2-.2l1.6.9c.5.3.6.9.2 1.4l-.6.8c-.5.5-1.2.7-1.9.4-2.6-1-4.6-3-5.6-5.6-.3-.7-.1-1.4.4-1.900z" fill="#000"/></svg>
      </li>
      <li>brightlanetidy@mailnest.example
        <svg class="icon" viewBox="0 0 20 20" aria-hidden="true"><circle cx="10" cy="10" r="10" fill="#6f9544"/><path d="M14.8 5.2 4.8 9.3l3.6 1.3 1.3 3.6z" fill="#000"/><path d="M8.4 10.6l3.2-2.8" stroke="#6f9544" stroke-width="0.9"/></svg>
      </li>
      <li>www.brightlanetidy.example
        <svg class="icon" viewBox="0 0 20 20" aria-hidden="true"><circle cx="10" cy="10" r="10" fill="#6f9544"/><g fill="none" stroke="#000" stroke-width="1.6" stroke-linecap="round"><path d="M9 11.6l-1.4 1.4a1.8 1.8 0 0 1-2.6-2.6L6.4 9"/><path d="M11 8.4l1.4-1.4a1.8 1.8 0 0 1 2.6 2.6L13.6 11"/><path d="M8.2 11.8l3.6-3.6"/></g></svg>
      </li>
      <li>Bonded &amp; Insured
        <svg class="icon" viewBox="0 0 20 20" aria-hidden="true"><circle cx="10" cy="10" r="10" fill="#6f9544"/><path d="M10 4.5a3.8 3.8 0 0 0-3.8 3.8c0 2.8 3.8 7 3.8 7s3.8-4.2 3.8-7A3.8 3.8 0 0 0 10 4.5z" fill="none" stroke="#000" stroke-width="1.4"/><circle cx="10" cy="8.3" r="1.3" fill="#000"/></svg>
      </li>
      <li class="no-icon">Alder Ridge, CO 80999</li>
    </ul>
  </section>

</main>
</body>
</html>
```